Theme for 60th Anniversary party for a Business

We are looking for a theme for our 60th year party. The theme we used for our 50th party was a movie premier with a drive-in movie. Info on our 50th party is here http://brookwingaero.com/about/50th-anniversary/. The theme must incorporate what we do as a business. Full website at www.brookwingaero.com. The theme would be expanded upon with the use of props or other items to make a large celebration. The party would have around 400 invited guests to take place at our business location on an airport. Please provide details of your theme along with potential props, activities, or other items that would make your theme work. A logo for the theme will also be needed and could be provided with the theme.
Updates

Target Market(s)

Customers, Vendors, Potential Customers

Industry/Entity Type

Movie

Requirements
Must have
• Activities that can take place during event.

```html
<!DOCTYPE html>
<html lang="en">
<head>
<meta charset="utf-8">
<title>50s Jet Age Hangar Party Zones</title>
<link rel="stylesheet" href="https://fonts.googleapis.com/css2?family=Francois+One&display=swap">
<style>
  :root {
    --ink: #130b0c;
    --paper: #ffffff;
    --text-light: #ffffff;
    --floor-light: #e6e6e6;
    --floor-mid: #9a9a9a;
    --floor-dark: #3a3a3a;
    --truss: #b4b4b4;
  }
  * { margin: 0; padding: 0; box-sizing: border-box; }
  html, body { width: 1200px; height: 1000px; overflow: hidden; background: var(--paper); }
  .canvas {
    position: relative;
    width: 1200px;
    height: 1000px;
    font-family: "Francois One", "Arial Narrow", sans-serif;
    text-transform: uppercase;
    color: var(--ink);
    letter-spacing: 0.6px;
  }
  .zone {
    position: absolute;
    border-radius: 50%;
    background: var(--ink);
    color: var(--text-light);
    display: flex;
    align-items: center;
    justify-content: center;
    text-align: center;
    font-size: 22px;
    line-height: 30px;
  }
  .zone--bar     { left: 34px;  top: 50px;  width: 290px; height: 290px; }
  .zone--games   { left: 814px; top: 12px;  width: 292px; height: 296px; }
  .zone--diner   { left: 36px;  top: 676px; width: 292px; height: 292px; }
  .zone--screen  { left: 830px; top: 668px; width: 280px; height: 296px; }
  .zone--bar p    { margin-top: -30px; }
  .zone--games p  { margin-top: -4px; }
  .zone--diner p  { margin-top: -4px; }
  .zone--screen p { margin-top: 18px; }

  .dot {
    position: absolute;
    width: 64px;
    height: 64px;
    border-radius: 50%;
    background: var(--ink);
  }
  .dot--planes-top    { left: 121px; top: 417px; }
  .dot--planes-bottom { left: 126px; top: 538px; }
  .dot--photo-top     { left: 959px; top: 393px; }
  .dot--photo-bottom  { left: 964px; top: 514px; }

  .label {
    position: absolute;
    text-align: center;
    font-size: 21px;
    line-height: 29px;
  }
  .label--lookalikes { left: 330px; top: 94px; width: 500px; font-size: 19px; }
  .label--lookalikes .gap { display: block; height: 23px; }
  .label--planes { left: 0; top: 480px; width: 320px; }
  .label--photo  { left: 850px; top: 466px; width: 290px; }

  .dance-floor {
    position: absolute;
    left: 352px;
    top: 292px;
    width: 460px;
    height: 460px;
  }
  .stage-label {
    position: absolute;
    left: 493px;
    top: 426px;
    width: 176px;
    height: 176px;
    border-radius: 50%;
    background: var(--ink);
    color: var(--text-light);
    display: flex;
    align-items: center;
    justify-content: center;
    text-align: center;
    font-size: 21px;
    line-height: 30px;
  }
</style>
</head>
<body>
<main class="canvas">
  <div class="zone zone--bar"><p>50's hangar<br>bar serving drinks</p></div>
  <div class="zone zone--games"><p>Games area,<br>flight sim/pool hall<br>jet age theme</p></div>
  <div class="zone zone--diner"><p>50's airfield diner<br>food/snacks and<br>drinks.</p></div>
  <div class="zone zone--screen"><p>Hangar door<br>screen area<br>with short 50's<br>flying films</p></div>

  <p class="label label--lookalikes">Pilots &amp; crew from the era to move around<br>the zones<span class="gap"></span>Including<br>Marlena Mayfair.</p>

  <span class="dot dot--planes-top"></span>
  <span class="dot dot--planes-bottom"></span>
  <p class="label label--planes">50's vintage aircraft<br>and pilot lookalikes</p>

  <span class="dot dot--photo-top"></span>
  <span class="dot dot--photo-bottom"></span>
  <p class="label label--photo">50's cockpit photo booths</p>

  <svg class="dance-floor" viewBox="0 0 460 460" role="img" aria-label="Round checkerboard dance floor inside a lighting truss ring with coloured stage light beams">
    <defs>
      <radialGradient id="floorTone" cx="50%" cy="50%" r="50%">
        <stop offset="0%" stop-color="#3a3a3a"/>
        <stop offset="70%" stop-color="#9a9a9a"/>
        <stop offset="100%" stop-color="#e6e6e6"/>
      </radialGradient>
    </defs>
    <circle cx="230" cy="230" r="204" fill="url(#floorTone)"/>
    <circle cx="230" cy="230" r="226" fill="none" stroke="#b4b4b4" stroke-width="3"/>
    <circle cx="230" cy="230" r="206" fill="none" stroke="#b4b4b4" stroke-width="3"/>
  </svg>

  <div class="stage-label"><p>Stage,<br>live band<br>&amp; surrounding<br>dance floor</p></div>
</main>
</body>
</html>
```